Need Business Card for our Indian Grocery Store

Industry/Entity Type

Grocery Store

Contact Information for Business Card

Manoj Baweja
Director

Store Locations:

Fernleigh
482 Elm Parade
P: 03 9172 5843

Ashvale
613 Carlow Road
P: 03 9238 6014

email: kvtmarts@mailnest.example

Requirements
Must have
• Our logo Colours

```html
<!DOCTYPE html>
<html lang="en">
<head>
<meta charset="utf-8">
<title>KVT Mart — Business Card</title>
<link href="https://fonts.googleapis.com/css2?family=Lato:wght@400;700;900&display=swap" rel="stylesheet">
<style>
  :root {
    --brand-red: #e8161b;
    --brand-red-faint: #ee2529;
    --card-white: #ffffff;
    --ink: #1f1f1f;
    --backdrop: #e6e4e1;
  }
  * { box-sizing: border-box; margin: 0; padding: 0; }
  html, body { width: 1200px; height: 843px; overflow: hidden; }
  body {
    background: var(--backdrop);
    font-family: "Lato", sans-serif;
    display: flex;
    align-items: center;
    justify-content: center;
    gap: 40px;
  }
  .card {
    width: 540px;
    height: 309px;
    position: relative;
    overflow: hidden;
    box-shadow: 0 6px 18px rgba(0,0,0,0.12);
  }

  /* Front */
  .card--front { background: var(--brand-red); }
  .front__watermark {
    position: absolute;
    left: 0;
    right: 0;
    top: 14px;
    text-align: center;
    font-weight: 900;
    font-size: 190px;
    letter-spacing: 16px;
    color: var(--brand-red-faint);
    line-height: 1;
    white-space: nowrap;
  }
  .front__watermark-sub {
    position: absolute;
    left: 0;
    right: 0;
    bottom: 20px;
    text-align: center;
    font-weight: 900;
    font-size: 30px;
    letter-spacing: 10px;
    color: var(--brand-red-faint);
    white-space: nowrap;
  }
  .front__lockup {
    position: absolute;
    inset: 0;
    display: flex;
    flex-direction: column;
    align-items: center;
    justify-content: center;
    gap: 8px;
    color: var(--card-white);
  }
  .brand-name {
    font-weight: 900;
    font-size: 46px;
    letter-spacing: 3px;
    text-transform: uppercase;
    line-height: 1.1;
  }
  .brand-tagline {
    display: flex;
    align-items: center;
    gap: 8px;
    font-size: 12px;
    letter-spacing: 0.5px;
    white-space: nowrap;
  }
  .brand-tagline::before, .brand-tagline::after {
    content: "";
    width: 18px;
    height: 1px;
    background: currentColor;
  }

  /* Back */
  .card--back { background: var(--card-white); color: var(--ink); }
  .back__person { position: absolute; left: 48px; top: 52px; }
  .person__name { color: var(--brand-red); font-weight: 700; font-size: 17px; }
  .person__role { font-size: 13px; margin-top: 3px; }
  .back__lockup {
    position: absolute;
    left: 48px;
    bottom: 62px;
    color: var(--brand-red);
    display: flex;
    flex-direction: column;
    align-items: center;
    gap: 6px;
  }
  .back__lockup .brand-name { font-size: 38px; }
  .back__lockup .brand-tagline { font-size: 11px; }
  .back__contact {
    position: absolute;
    left: 300px;
    top: 88px;
    font-size: 11.5px;
    line-height: 1.4;
    white-space: nowrap;
  }
  .contact__group { margin-bottom: 12px; }
  .contact__label { color: var(--brand-red); font-size: 11px; }
</style>
</head>
<body>
  <section class="card card--front" aria-label="Card front">
    <div class="front__watermark" aria-hidden="true">KVT</div>
    <div class="front__watermark-sub" aria-hidden="true">KVT MART</div>
    <div class="front__lockup">
      <div class="brand-name">KVT Mart</div>
      <div class="brand-tagline">Fresh Pantry Since 2011</div>
    </div>
  </section>

  <section class="card card--back" aria-label="Card back">
    <div class="back__person">
      <div class="person__name">Manoj Baweja</div>
      <div class="person__role">Director</div>
    </div>
    <div class="back__lockup">
      <div class="brand-name">KVT Mart</div>
      <div class="brand-tagline">Fresh Pantry Since 2011</div>
    </div>
    <div class="back__contact">
      <div class="contact__group">
        <div class="contact__label">Store Locations:</div>
        <div>Fernleigh 482 Elm Parade</div>
        <div>P: 03 9172 5843</div>
      </div>
      <div class="contact__group">
        <div class="contact__label">Ashvale</div>
        <div>613 Carlow Road</div>
        <div>P: 03 9238 6014</div>
      </div>
      <div class="contact__group">
        <div class="contact__label">Email:</div>
        <div>kvtmarts@mailnest.example</div>
      </div>
    </div>
  </section>
</body>
</html>
```